Business card design and logo needed - Photographer

I take photos of weddings, rodeos, snowmobiling.
Need a card to hand out to prospective clients.
Industry/Entity Type
Business
Contact Information for Business Card
Marcus Dolven Photography
Requirements
Must have
- Bold
Black or white base.
My website. www.MarcusDolven.example
Should not have
- camera/ lens/ aperture blades

```html
<!DOCTYPE html>
<html lang="en">
<head>
<meta charset="utf-8">
<title>Marcus Dolven Photography – Business Card</title>
<link rel="stylesheet" href="https://fonts.googleapis.com/css2?family=Saira+Extra+Condensed:wght@500;700&display=swap">
<style>
  :root {
    --paper: #ffffff;
    --card: #000000;
    --ink: #ffffff;
  }
  html, body {
    margin: 0;
    padding: 0;
    width: 1200px;
    height: 693px;
    overflow: hidden;
    background: var(--paper);
  }
  .canvas {
    display: block;
    width: 1200px;
    height: 693px;
  }
  .card { fill: var(--card); }
  .brand-mark__circle {
    fill: none;
    stroke: var(--ink);
    stroke-width: 8;
  }
  .brand-mark__name,
  .identity__name,
  .contact {
    fill: var(--ink);
    font-family: "Saira Extra Condensed", "Arial Narrow", sans-serif;
  }
  .brand-mark__name {
    font-weight: 700;
    font-size: 34px;
  }
  .identity__name {
    font-weight: 700;
    font-size: 144px;
  }
  .contact {
    font-weight: 500;
  }
  .contact--phone { font-size: 32px; }
  .contact--web { font-size: 30px; }
</style>
</head>
<body>
<svg class="canvas" viewBox="0 0 1200 693" xmlns="http://www.w3.org/2000/svg">
  <title>Marcus Dolven Photography</title>
  <rect class="card" x="29" y="29" width="1145" height="643"/>

  <g class="brand-mark">
    <circle class="brand-mark__circle" cx="281" cy="315" r="62"/>
    <text class="brand-mark__name" x="211" y="430" textLength="140" lengthAdjust="spacing">DOLVEN</text>
  </g>

  <g class="identity">
    <text class="identity__name" x="488" y="272" textLength="538" lengthAdjust="spacingAndGlyphs">MARCUS DOLVEN</text>
    <text class="identity__name" x="488" y="411" textLength="575" lengthAdjust="spacingAndGlyphs">PHOTOGRAPHY</text>
  </g>

  <g class="contact-block">
    <text class="contact contact--phone" x="486" y="480" textLength="365" lengthAdjust="spacing">(306) 555 0142</text>
    <text class="contact contact--web" x="486" y="545" textLength="640" lengthAdjust="spacing">WWW.MARCUSDOLVEN.EXAMPLE</text>
  </g>
</svg>
</body>
</html>
```